We need a set of stationary to compliment our new logo including letterhead (A4 & A5), envelopes, Business cards and appointment cards.

Hi Designers - our details are set out below.
Larchvale Family Medical
Shop 7, 62-64 Dunmore Avenue
GAWLER EAST SA 5118
Phone - 08 84716392
Fax - 08 84716397
www.larchvalefm.com.au

Cheers Tess

Industry/Entity Type

Medical

Requirements
Must have
• Reflect the logo be modern and classy

```html
<!DOCTYPE html>
<html lang="en">
<head>
<meta charset="utf-8">
<title>Larchvale Family Medical – Stationery</title>
<link href="https://fonts.googleapis.com/css2?family=Questrial&family=Dancing+Script&display=swap" rel="stylesheet">
<style>
:root{
  --bg:#e4e0da;
  --paper:#f4f4f3;
  --paper-edge:#d6d6d4;
  --ink:#2b2b2b;
  --brand-blue:#2a6db5;
  --brand-green:#7bb83a;
  --band:#bfe8e6;
}
*{margin:0;padding:0;box-sizing:border-box}
html,body{width:1200px;height:1096px;overflow:hidden}
body{background:var(--bg);font-family:"Questrial",sans-serif;color:var(--ink);position:relative}
.piece{position:absolute;background:var(--paper);box-shadow:0 1px 3px rgba(0,0,0,.25)}

/* brand name lockup */
.brand{display:flex;flex-direction:column;align-items:center;color:var(--brand-blue);line-height:1}
.brand .dot{width:26px;height:26px;border-radius:50%;background:var(--brand-green);margin-bottom:6px}
.brand .name{font-size:22px;letter-spacing:.5px}
.brand .sub{font-size:7px;letter-spacing:2px;margin-top:2px;align-self:flex-end}

/* business card front */
.card-front{width:178px;height:97px;display:flex;justify-content:center;align-items:center}
.card-front--a{left:99px;top:372px}
.card-front--b{left:338px;top:600px}

/* appointment card */
.appt{left:359px;top:370px;width:179px;height:100px;padding:8px 12px;font-size:9px}
.appt h3{text-align:center;font-size:9px;font-weight:bold;margin-bottom:10px}
.appt .field{display:flex;align-items:flex-end;margin-bottom:8px;gap:2px}
.appt .line{flex:1;border-bottom:1px solid #333;height:1px}
.appt .doc{text-align:center;font-size:7px;margin-top:6px}
.appt .fine{font-size:4.5px;text-align:center;margin-top:4px;line-height:1.5}

/* business card back */
.card-back{left:337px;top:767px;width:179px;height:96px}
.card-back .brand{position:absolute;left:10px;top:28px}
.card-back .brand .dot{width:16px;height:16px}
.card-back .brand .name{font-size:10px}
.card-back .brand .sub{font-size:4px}
.card-back .person{position:absolute;left:96px;top:8px;font-size:8px;text-align:center}
.card-back .person b{display:block;font-size:7px;margin-top:4px}
.card-back .contact{position:absolute;right:8px;top:36px;font-size:4.5px;line-height:1.7}
.card-back .contact b{display:inline-block;width:20px;text-align:right;margin-right:3px}

/* letterhead */
.letterhead{left:622px;top:109px;width:410px;height:577px}
.letterhead .brand{position:absolute;left:14px;top:14px;align-items:flex-start}
.letterhead .brand .dot{margin-left:58px}
.letterhead .brand .name{font-size:17px}
.letterhead .web{position:absolute;left:12px;top:75px;font-size:10px;color:var(--brand-blue);font-weight:bold}
.letterhead .contact{position:absolute;right:6px;top:17px;font-size:11px;line-height:18.5px}
.letterhead .contact b{display:inline-block;width:86px;text-align:right;margin-right:4px}
.letterhead .body{position:absolute;left:75px;top:154px;width:268px;font-size:12px;line-height:10px;color:#1f1f1f}
.letterhead .body p{text-indent:18px;margin-bottom:10px}
.letterhead .sign{position:absolute;left:296px;top:488px;font-size:12px}
.letterhead .signature{position:absolute;left:306px;top:508px;font-family:"Dancing Script",cursive;font-size:12px}
.letterhead .rule{position:absolute;left:31px;right:27px;top:557px;border-top:1px solid var(--brand-green)}
.letterhead .address{position:absolute;left:0;right:0;text-align:center;top:563px;font-size:10px}

/* envelopes */
.env-front{left:790px;top:822px;width:312px;height:219px}
.env-front .brand{position:absolute;left:118px;top:0;align-items:flex-start}
.env-front .brand .name{font-size:22px}
.env-front .web{position:absolute;left:140px;top:94px;font-size:10px;color:var(--brand-green)}
.env-front .person{position:absolute;left:16px;top:172px;font-size:10px}
.env-front .person b{display:block;margin-top:6px;margin-left:12px}
.env-front .contact{position:absolute;right:8px;top:168px;font-size:7px;line-height:1.55}
.env-back{left:626px;top:752px;width:312px;height:222px;overflow:hidden}
.env-back svg.flap{position:absolute;inset:0}
.env-back .band{position:absolute;left:97px;top:0;width:117px;height:222px;background:var(--band);opacity:.9}
.env-back .brand{position:absolute;left:100px;top:14px}
.env-back .brand .name{font-size:15px}
.env-back .brand .sub{font-size:5px}
.env-back .web{position:absolute;left:97px;top:205px;width:117px;text-align:center;font-size:9px;color:var(--brand-blue)}
</style>
</head>
<body>

<div class="piece card-front card-front--a">
  <div class="brand"><span class="dot"></span><span class="name">LARCHVALE</span><span class="sub">FAMILY MEDICAL</span></div>
</div>

<div class="piece appt">
  <h3>APPOINTMENT</h3>
  <div class="field">NAME:<span class="line"></span></div>
  <div class="field">DATE:<span class="line"></span>TIME:<span class="line"></span></div>
  <div class="doc">John Doe <b>MD</b></div>
  <div class="fine"><b>phone:</b> 08 84716392 &nbsp; <b>email:</b> larchvale@net.com<br>Shop 7, 62-64 Dunmore Avenue, Gawler East SA 5118</div>
</div>

<div class="piece card-front card-front--b">
  <div class="brand"><span class="dot"></span><span class="name">LARCHVALE</span><span class="sub">FAMILY MEDICAL</span></div>
</div>

<div class="piece card-back">
  <div class="brand"><span class="dot"></span><span class="name">LARCHVALE</span><span class="sub">FAMILY MEDICAL</span></div>
  <div class="person">John Doe<b>MD</b></div>
  <div class="contact">
    <div><b>phone:</b>08 84716392</div>
    <div><b>fax:</b>08 84716397</div>
    <div><b>mobile:</b>0412 375 908</div>
    <div><b>email:</b>larchvale@net.com</div>
    <div><b>web:</b>www.larchvalefm.com.au</div>
    <div><b>address:</b>Shop 7, 62-64 Dunmore Avenue,</div>
    <div><b></b>Gawler East SA 5118</div>
  </div>
</div>

<div class="piece letterhead">
  <div class="brand"><span class="dot"></span><span class="name">LARCHVALE</span><span class="sub">FAMILY MEDICAL</span></div>
  <div class="web">www.larchvalefm.com.au</div>
  <div class="contact">
    <div><b>phone:</b>08 84716392</div>
    <div><b>fax:</b>08 84716397</div>
    <div><b>mobile:</b>0412 375 908</div>
    <div><b>email:</b>larchvale@net.com</div>
  </div>
  <div class="body">
    <p>Lorem ipsum dolor sit amet, consectetuer adipiscing elit, sed diam nonummy nibh euismod tincidunt ut laoreet dolore magna aliquam erat volutpat. Ut wisi enim ad minim veniam, quis nostrud exerci tation ullamcorper suscipit lobortis nisl ut aliquip ex ea commodo consequat.</p>
    <p>Duis autem vel eum iriure dolor in hendrerit in vulputate velit esse molestie consequat, vel illum dolore eu feugiat nulla facilisis at vero eros et accumsan et iusto odio dignissim qui blandit praesent luptatum zzril delenit augue duis dolore te feugait nulla facilisi. Nam liber tempor cum soluta nobis eleifend option congue nihil imperdiet doming id quod mazim placerat facer possim assum. Typi non habent claritatem insitam; est usus legentis in iis qui facit eorum claritatem.</p>
    <p>Investigationes demonstraverunt lectores legere me lius quod ii legunt saepius. Claritas est etiam processus dynamicus, qui sequitur mutationem consuetudium lectorum. Mirum est notare quam littera gothica, quam nunc putamus parum claram, anteposuerit litterarum formas humanitatis per seacula quarta decima et quinta decima. Eodem modo typi, qui nunc nobis videntur parum clari, fiant sollemnes in futurum.</p>
  </div>
  <div class="sign">John Doe</div>
  <div class="signature">John Doe</div>
  <div class="rule"></div>
  <div class="address"><b>address:</b> Shop 7, 62-64 Dunmore Avenue, Gawler East SA 5118</div>
</div>

<div class="piece env-front">
  <div class="brand"><span class="dot"></span><span class="name">LARCHVALE</span><span class="sub">FAMILY MEDICAL</span></div>
  <div class="web">www.larchvalefm.com.au</div>
  <div class="person">John Doe<b>MD</b></div>
  <div class="contact">08 84716392<br>larchvale@net.com<br><br>Shop 7, 62-64 Dunmore Avenue,<br>Gawler East SA 5118</div>
</div>

<div class="piece env-back">
  <svg class="flap" width="312" height="222" viewBox="0 0 312 222">
    <polyline points="0,0 130,130 182,130 312,0" fill="none" stroke="var(--paper-edge)" stroke-width="1"/>
    <polyline points="0,222 150,120 312,222" fill="none" stroke="var(--paper-edge)" stroke-width="1"/>
  </svg>
  <div class="band" role="img" aria-label="Pale teal band with a faint geometric pattern"></div>
  <div class="brand"><span class="dot"></span><span class="name">LARCHVALE</span><span class="sub">FAMILY MEDICAL</span></div>
  <div class="web">www.larchvalefm.com.au</div>
</div>

</body>
</html>
```